Halvorn spray foam and Environmental

I have business cards but need new ones. The ones I have are very bland. Here is. Y company website http://www.halvornsprayfoam.ca

Also I can send you copies of the current cards
I would also need my current logo on the new design as well.. Also spray foam and Environmental

Industry/Entity Type

Business

Logo Text

Halvorn.

```html
<!DOCTYPE html>
<html lang="en">
<head>
<meta charset="utf-8">
<title>Halvorn Business Card</title>
<link rel="stylesheet" href="https://fonts.googleapis.com/css2?family=Open+Sans:wght@700&family=Michroma&family=Work+Sans:wght@400;500&display=swap">
<style>
  :root {
    --stage: #e4e4e4;
    --card-dark: #000000;
    --card-light: #ffffff;
    --purple: #7b3fa0;
    --purple-deep: #4f2168;
    --slate: #3a3d4a;
    --text-grey: #555860;
    --rule: #cfcfcf;
    --band-grey: #b9b9b9;
    --top-edge: #bfe3f2;
  }
  * { margin: 0; padding: 0; box-sizing: border-box; }
  html, body { width: 1200px; height: 1000px; overflow: hidden; background: var(--stage); }
  .canvas { position: relative; width: 1200px; height: 1000px; }

  .card { position: absolute; left: 261px; width: 654px; height: 373px; overflow: hidden; }

  /* Front card */
  .card-front { top: 108px; background: var(--card-dark); }
  .brand-front { position: absolute; left: 119px; top: 33px; height: 87px; display: flex; align-items: center; gap: 23px; }
  .brand-mark { display: block; background: var(--purple); }
  .brand-front .brand-mark { width: 107px; height: 87px; }
  .brand-front .brand-name { font-family: "Open Sans", sans-serif; font-weight: 700; font-size: 44px; letter-spacing: 6px; color: #fff; }
  .rule { position: absolute; background: var(--rule); }
  .rule-h1 { left: 0; top: 159px; width: 654px; height: 2px; }
  .rule-h2 { left: 0; top: 217px; width: 654px; height: 2px; }
  .rule-v { left: 326px; top: 159px; width: 2px; height: 214px; }
  .service-title { position: absolute; top: 178px; font-family: "Michroma", sans-serif; font-size: 17.5px; font-weight: 400; color: var(--purple); letter-spacing: 2.6px; -webkit-text-stroke: 1px var(--purple); line-height: 22px; white-space: nowrap; }
  .title-spray { left: 39px; }
  .title-enviro { left: 359px; letter-spacing: 2.2px; }
  .service-list { position: absolute; top: 232px; list-style: none; font-family: "Work Sans", sans-serif; font-size: 15.5px; letter-spacing: 2.6px; color: #fff; line-height: 20.3px; }
  .service-list li { position: relative; padding-left: 23px; }
  .service-list li::before { content: ""; position: absolute; left: 0; top: 7px; width: 7px; height: 7px; border-radius: 50%; background: var(--purple); }
  .list-spray { left: 38px; }
  .list-enviro { left: 362px; }

  /* Back card */
  .card-back { top: 518px; background: var(--card-light); border-top: 2px solid var(--top-edge); }
  .brand-back { position: absolute; left: 0; top: 54px; width: 654px; text-align: center; }
  .brand-back .brand-mark { width: 78px; height: 64px; margin: 0 auto; }
  .brand-back .brand-name { display: block; margin-top: 13px; font-family: "Open Sans", sans-serif; font-weight: 700; font-size: 30px; letter-spacing: 5px; color: var(--slate); line-height: 1; }
  .divider { position: absolute; left: 325px; top: 186px; width: 2px; height: 102px; background: var(--slate); }
  .contact { position: absolute; top: 192px; font-family: "Work Sans", sans-serif; }
  .contact h2 { font-weight: 400; font-size: 19px; color: #2e3038; letter-spacing: 0.3px; margin-bottom: 8px; }
  .contact ul { list-style: none; font-size: 15px; color: var(--text-grey); line-height: 21px; }
  .contact li { display: flex; align-items: center; gap: 9px; }
  .contact-enviro { right: 354px; text-align: right; }
  .contact-enviro h2 { margin-right: 18px; }
  .contact-enviro li { justify-content: flex-end; }
  .contact-spray { left: 359px; }
  .icon { width: 9px; height: 9px; fill: none; stroke: var(--purple); stroke-width: 1.5; flex: none; }
  .address-band { position: absolute; left: 0; bottom: 0; width: 654px; height: 26px; }
  .address { position: absolute; left: 134px; bottom: 5px; width: 396px; text-align: center; font-family: "Work Sans", sans-serif; font-size: 13.5px; color: #fff; letter-spacing: 0.2px; white-space: nowrap; line-height: 16px; }
</style>
</head>
<body>
<main class="canvas">

  <section class="card card-front" aria-label="Card front">
    <div class="brand-front">
      <span class="brand-mark"></span>
      <span class="brand-name">HALVORN</span>
    </div>
    <div class="rule rule-h1"></div>
    <div class="rule rule-h2"></div>
    <div class="rule rule-v"></div>
    <h2 class="service-title title-spray">SPRAY FOAM</h2>
    <h2 class="service-title title-enviro">ENVIRONMENTAL</h2>
    <ul class="service-list list-spray">
      <li>ROOFING FOAM</li>
      <li>SLABJACKING</li>
      <li>2POUND/HALF POUND</li>
      <li>SOUND PROOFING</li>
      <li>BATT INSULATION</li>
      <li>ATTIC BLOW IN</li>
    </ul>
    <ul class="service-list list-enviro">
      <li>ROOFING FOAM</li>
      <li>SLABJACKING</li>
      <li>2POUND/HALF POUND</li>
      <li>SOUND PROOFING</li>
      <li>BATT INSULATION</li>
      <li>ATTIC BLOW IN</li>
    </ul>
  </section>

  <section class="card card-back" aria-label="Card back">
    <svg width="0" height="0" style="position:absolute">
      <defs>
        <symbol id="icon-phone" viewBox="0 0 10 10"><path d="M2 1 L3.5 1 L4 3 L3 3.8 Q4 6 6.2 7 L7 6 L9 6.5 L9 8 Q8.5 9 7.5 9 Q1 8 1 2 Q1 1 2 1 Z"/></symbol>
        <symbol id="icon-mail" viewBox="0 0 10 10"><rect x="1" y="2" width="8" height="6"/><path d="M1 2 L5 5.5 L9 2"/></symbol>
        <symbol id="icon-globe" viewBox="0 0 10 10"><circle cx="5" cy="5" r="4"/><path d="M1 5 H9 M5 1 Q2.5 5 5 9 M5 1 Q7.5 5 5 9"/></symbol>
      </defs>
    </svg>

    <div class="brand-back">
      <span class="brand-mark"></span>
      <span class="brand-name">HALVORN</span>
    </div>
    <div class="divider"></div>

    <div class="contact contact-enviro">
      <h2>ENVIRONMENTAL</h2>
      <ul>
        <li>604-555-0193 <svg class="icon"><use href="#icon-phone"/></svg></li>
        <li>enviro1@halvornmail.com <svg class="icon"><use href="#icon-mail"/></svg></li>
        <li>www.halvornsprayfoam.ca <svg class="icon"><use href="#icon-globe"/></svg></li>
      </ul>
    </div>

    <div class="contact contact-spray">
      <h2>SPRAY FOAM</h2>
      <ul>
        <li><svg class="icon"><use href="#icon-phone"/></svg> 604-555-0147</li>
        <li><svg class="icon"><use href="#icon-mail"/></svg> halvornfoam@mailbox.com</li>
        <li><svg class="icon"><use href="#icon-globe"/></svg> www.halvornsprayfoam.ca</li>
      </ul>
    </div>

    <svg class="address-band" viewBox="0 0 654 26" preserveAspectRatio="none" aria-hidden="true">
      <polygon points="0,0 104,0 124,26 0,26" fill="var(--purple-deep)"/>
      <polygon points="112,0 544,0 526,26 132,26" fill="var(--band-grey)"/>
      <polygon points="562,0 654,0 654,26 542,26" fill="var(--purple-deep)"/>
    </svg>
    <p class="address">118 Kestrel Ave Burnaby, British Columbia v5g 0z9, CA</p>
  </section>

</main>
</body>
</html>
```